Beatrices Business Card

Looking for business card that is PROFESSIONAL yet has a flair of design. My colors are white with black font. My last name is Harwell so a tiara could be faded in the background OR embossed. I would love my pic to be in a frame with an interesting background/texture. Fonts need to be CLASSY, not cheesy. I need ALL verbiage included but can be on both back and front.

Beatrice Harwell
Real Estate Agent
720-555-0183 bharwell@dovrealty.example

Accredited Highland Property Advisor
Accredited Premier Residence Promotion Advisor
Accredited Dealmaking Professional

DOV/RE Summit
41275 Thornbury Blvd 303-555-218 Each office indepdendly owned and operated

Target Market(s)

Sellers and Buyers. Millennials on up

Industry/Entity Type

Real Estate Agent

Contact Information for Business Card

Beatrice Harwell
Real Estate Agent

DOV/RE Summit
41275 Thornbury Blvd 303-555-218
Each office independently owned and operated

Font styles to use
Serif

Colors
f04a50
ffffff
000000

Requirements
Must have
• a classy, fun feel to it. Unique, high end. But it has to look professional and be taken seriously.
Nice to have
• Elegant, classy, fun.
Should not have
• anything cheesy or tacky.

```html
<!DOCTYPE html>
<html lang="en">
<head>
<meta charset="utf-8">
<title>Beatrice Harwell – Business Card</title>
<link rel="stylesheet" href="https://fonts.googleapis.com/css2?family=Cinzel:wght@600&family=Oswald:wght@600&family=Open+Sans:wght@400&display=swap">
<style>
  :root {
    --backdrop: #ececea;
    --card-dark: #1f1d1e;
    --card-light: #ffffff;
    --ink: #231f20;
    --accent: #d7121d;
    --silver: #a9a9a9;
    --hair: #b7845c;
    --skin: #c9a07f;
    --top: #c8202a;
    --top-deep: #b81822;
  }
  * { margin: 0; padding: 0; box-sizing: border-box; }
  html, body { width: 1200px; height: 1000px; overflow: hidden; }
  body { background: var(--backdrop); position: relative; font-family: "Open Sans", Arial, sans-serif; color: var(--ink); }

  .card { position: absolute; left: 266px; width: 666px; height: 397px; overflow: hidden; }

  .card-front { top: 75px; background: var(--card-dark); }
  .front-name {
    position: absolute; left: 0; right: 0; top: 206px;
    text-align: center;
    font-family: "Cinzel", Georgia, serif; font-weight: 600;
    font-size: 41px; letter-spacing: 0.5px;
    color: var(--silver);
  }

  .card-back { top: 533px; background: var(--card-light); }
  .accent-bar { position: absolute; left: 0; top: 67px; width: 16px; height: 50px; background: var(--accent); }
  .agent-name {
    position: absolute; left: 34px; top: 60px;
    font-family: "Oswald", "Arial Narrow", sans-serif; font-weight: 600;
    font-size: 30px; line-height: 1.1; letter-spacing: -0.3px;
    text-transform: uppercase; color: var(--ink);
  }
  .agent-title { position: absolute; left: 34px; top: 97px; font-size: 18px; color: var(--accent); }

  .contact { position: absolute; left: 34px; top: 147px; list-style: none; font-size: 16px; line-height: 22px; }
  .contact li { display: flex; align-items: center; gap: 5px; }
  .contact svg { width: 14px; height: 12px; fill: var(--accent); }

  .credentials { position: absolute; left: 34px; top: 206px; font-size: 16.5px; line-height: 20.5px; white-space: nowrap; }
  .office { position: absolute; left: 34px; top: 279px; font-size: 16.5px; line-height: 20.5px; white-space: nowrap; }
  .office .office-name { margin-bottom: 3px; }

  .portrait { position: absolute; left: 0; top: 0; width: 666px; height: 397px; }
  .portrait-head {
    position: absolute; left: 414px; top: 14px; width: 252px; height: 300px;
    border-radius: 126px 126px 0 0;
    background: linear-gradient(180deg, var(--hair) 0%, var(--skin) 60%, var(--top) 100%);
  }
  .portrait-body {
    position: absolute; left: 318px; top: 285px; width: 348px; height: 112px;
    border-radius: 90px 0 0 0;
    background: linear-gradient(180deg, var(--top) 0%, var(--top-deep) 100%);
  }
</style>
</head>
<body>
  <section class="card card-front" aria-label="Card front">
    <div class="front-name">BEATRICE HARWELL</div>
  </section>

  <section class="card card-back" aria-label="Card back">
    <div class="portrait" role="img" aria-label="Portrait photo of the agent in a red top">
      <div class="portrait-head"></div>
      <div class="portrait-body"></div>
    </div>

    <div class="accent-bar"></div>
    <h1 class="agent-name">Beatrice Harwell</h1>
    <p class="agent-title">Real Estate Agent</p>

    <ul class="contact">
      <li>
        <svg viewBox="0 0 14 12" aria-hidden="true"><path d="M1 4.5C1 2 4 1 7 1s6 1 6 3.5l-3 .8-.6-1.8H4.6L4 5.3zM3.5 6h7l1.5 5H2z"/></svg>
        720-555-0183
      </li>
      <li>
        <svg viewBox="0 0 14 12" aria-hidden="true"><path d="M0 1.5h14v9H0zM1 2.5 7 7l6-4.5z" fill-rule="evenodd"/></svg>
        bharwell@dovrealty.example
      </li>
    </ul>

    <div class="credentials">
      <p>Accredited Highland Property Advisor</p>
      <p>Accredited Premier Residence Promotion Advisor</p>
      <p>Accredited Dealmaking Professional</p>
    </div>

    <div class="office">
      <p class="office-name">DOV/RE Summit</p>
      <p>41275 Thornbury Blvd 303-555-218</p>
      <p>Each office independently owned</p>
      <p>and operated</p>
    </div>
  </section>
</body>
</html>
```